Delia Morvan
exclusive handcrafted jewelry
Simple
delmorvan@quillbox.net
deliamorvandesign.net
business card should be shaded black like uploaded logo.
I also like the royal blue option !
I have no idea what is on that file since I can not open it . I hope it is my logo in blue or shaded black.

```html
<!DOCTYPE html>
<html lang="en">
<head>
<meta charset="utf-8">
<title>Delia Morvan — Business Card Options</title>
<link href="https://fonts.googleapis.com/css2?family=Arimo:wght@400;700&family=Allura&display=swap" rel="stylesheet">
<style>
  :root {
    --backdrop: #b86a2e;
    --ink-white: #ffffff;
    --ink-dark: #1a1a1a;
    --black-top: #2e2e2e;
    --black-bottom: #050505;
    --royal-top: #4a1a6e;
    --royal-bottom: #1e0530;
    --night-top: #2a0c40;
    --night-bottom: #050208;
    --silver-top: #ffffff;
    --silver-bottom: #c9c9c9;
    --strip-light: #e6e6e6;
    --strip-dark: #0c0c0c;
    --lime: #a8e21a;
  }
  * { box-sizing: border-box; margin: 0; padding: 0; }
  html, body {
    width: 1200px; height: 763px; overflow: hidden;
    background: var(--backdrop);
    font-family: "Arimo", Arial, sans-serif;
  }
  .canvas { position: relative; width: 1200px; height: 763px; }

  .card {
    position: absolute; width: 403px; height: 228px; overflow: hidden;
    box-shadow: 0 6px 14px rgba(0,0,0,.35);
  }
  .card--black  { left: 53px;  top: 67px;  background: linear-gradient(180deg, var(--black-top), var(--black-bottom)); color: var(--ink-white); }
  .card--royal  { left: 643px; top: 72px;  background: linear-gradient(180deg, var(--royal-top), var(--royal-bottom)); color: var(--ink-white); }
  .card--night  { left: 132px; top: 413px; background: linear-gradient(180deg, var(--night-top), var(--night-bottom)); color: var(--ink-white); }
  .card--silver { left: 737px; top: 422px; background: linear-gradient(180deg, var(--silver-top), var(--silver-bottom)); color: var(--ink-dark); }

  .card__text { position: absolute; font-size: 13px; letter-spacing: .2px; white-space: nowrap; }

  .brand {
    position: absolute; display: flex; align-items: center; gap: 8px;
    font-size: 22px; font-weight: 700; white-space: nowrap;
  }
  .brand__dot { width: 14px; height: 14px; border-radius: 50%; background: currentColor; }

  .name-script { position: absolute; font-family: "Allura", cursive; font-size: 36px; line-height: 1; white-space: nowrap; }
  .name-plain  { position: absolute; font-size: 27px; line-height: 1; white-space: nowrap; }
  .name-plain--bold { font-weight: 700; }

  .strip {
    position: absolute; left: 0; right: 0; bottom: 0; height: 26px;
    display: flex; justify-content: space-between; align-items: center;
    padding: 0 22px; font-size: 13px;
  }
  .strip--light { background: var(--strip-light); color: var(--ink-dark); }
  .strip--dark  { background: var(--strip-dark); color: var(--ink-white); }

  .lime { color: var(--lime); }
</style>
</head>
<body>
<main class="canvas">

  <section class="card card--black" aria-label="Black card option">
    <p class="card__text" style="left:24px; top:20px;">deliamorvandesign.net</p>
    <div class="brand" style="left:200px; top:44px;"><span class="brand__dot"></span>Delia Morvan</div>
    <p class="name-script" style="left:34px; top:102px;">Delia Morvan</p>
    <p class="card__text" style="left:262px; top:113px;">305-555-0172</p>
    <p class="card__text" style="right:18px; top:190px;">delmorvan@quillbox.net</p>
  </section>

  <section class="card card--royal" aria-label="Royal purple card option">
    <div class="brand" style="left:130px; top:30px;"><span class="brand__dot"></span>Delia Morvan</div>
    <p class="name-plain name-plain--bold" style="left:30px; top:150px;">Delia Morvan</p>
    <p class="card__text" style="left:245px; top:160px;">305-555-0172</p>
    <div class="strip strip--light">
      <span>deliamorvandesign.net</span>
      <span>delmorvan@quillbox.net</span>
    </div>
  </section>

  <section class="card card--night" aria-label="Dark purple card option">
    <p class="card__text" style="left:24px; top:20px;">deliamorvandesign.net</p>
    <div class="brand" style="left:200px; top:44px;"><span class="brand__dot"></span>Delia Morvan</div>
    <p class="name-script lime" style="left:28px; top:126px;">Delia Morvan</p>
    <p class="card__text" style="left:250px; top:138px;">305-555-0172</p>
    <p class="card__text" style="right:18px; top:194px;">delmorvan@quillbox.net</p>
  </section>

  <section class="card card--silver" aria-label="Silver card option">
    <div class="brand" style="left:120px; top:40px;"><span class="brand__dot"></span>Delia Morvan</div>
    <p class="name-plain" style="left:30px; top:136px;">Delia Morvan</p>
    <p class="card__text" style="left:232px; top:144px;">305-555-0172</p>
    <div class="strip strip--dark">
      <span>deliamorvandesign.net</span>
      <span>delmorvan@quillbox.net</span>
    </div>
  </section>

</main>
</body>
</html>
```